New business card design needed for Diesel Fitting (Mechanical) Company

We need a new business card for our company called "Gumtree Engine Works" that showcases our logo and business details.
Target Market(s)
Owners of all makes and models of vehicles, trucks, plant and machinery.
Industry/Entity Type
Mechanical
Contact Information for Business Card
The business card details need to include the following: Owners/Directors: Doug & Marisol Brent-Coyle ABN: 41 917 302 846 Address: 317 Wattlebrook Street CHARTERS TOWERS QLD 4820 Postal Address: PO Box 5791 CHARTERS TOWERS QLD 4820 Website: www.gewservice.com.au Phone: 4712 9083 Mobile: 0438 175 906 Emails: sales@gewservice.com.au; admin@gewservice.com.au; accounts@gewservice.com.au; parts@gewservice.com.au; office@gewservice.com.au, reception@gewservice.com.au
Look and feel

```html
<!DOCTYPE html>
<html lang="en">
<head>
<meta charset="utf-8">
<title>Gumtree Engine Works – Business Card</title>
<link rel="stylesheet" href="https://fonts.googleapis.com/css2?family=Didact+Gothic&family=Poppins:wght@500;600;700&display=swap">
<style>
  :root {
    --orange: #ec6e22;
    --orange-deep: #e0621b;
    --ink: #141414;
    --charcoal: #1c1c1c;
    --grey: #9a9a9a;
    --paper: #f7f7f7;
    --page: #e6e6e6;
    --white: #ffffff;
  }
  * { margin: 0; padding: 0; box-sizing: border-box; }
  html, body { width: 1200px; height: 2203px; overflow: hidden; }
  body { background: var(--page); position: relative; font-family: "Didact Gothic", sans-serif; }

  .card {
    position: absolute; left: 100px; width: 1000px; height: 572px; overflow: hidden;
    box-shadow: 0 6px 14px rgba(0,0,0,.35);
  }

  /* Front */
  .card-front { top: 490px; background: radial-gradient(ellipse at 50% 45%, #262626 0%, #0d0d0d 55%, #040404 100%); }
  .brand-front {
    position: absolute; left: 0; right: 0; top: 250px;
    display: flex; align-items: center; justify-content: center; gap: 18px;
  }
  .brand-dot { width: 38px; height: 38px; border-radius: 50%; background: var(--orange); }
  .brand-name {
    font-family: "Poppins", sans-serif; font-weight: 600; color: var(--orange);
    font-size: 52px; letter-spacing: .5px;
  }
  .front-dots { position: absolute; left: 0; right: 0; top: 455px; text-align: center; color: var(--orange); font-size: 26px; letter-spacing: 3px; line-height: 1; font-family: "Poppins", sans-serif; font-weight: 700; }
  .front-web {
    position: absolute; left: 0; right: 0; top: 486px; text-align: center;
    color: #e8e8e8; font-size: 27px; letter-spacing: 5px;
  }
  .front-web strong { color: var(--orange); font-family: "Poppins", sans-serif; font-weight: 700; }
  .front-band { position: absolute; left: 0; bottom: 0; width: 1000px; height: 18px; }

  /* Back */
  .card-back { top: 1122px; background: var(--paper); }
  .back-panel {
    position: absolute; left: 517px; top: 0; width: 483px; height: 572px;
    background: linear-gradient(160deg, var(--orange) 0%, var(--orange-deep) 100%);
  }
  .panel-notch { position: absolute; left: 517px; top: 78px; width: 22px; height: 36px; }

  .back-id { position: absolute; left: 0; width: 517px; text-align: center; color: var(--ink); }
  .brand-back {
    position: absolute; left: 0; width: 517px; top: 130px;
    display: flex; align-items: center; justify-content: center; gap: 14px;
  }
  .brand-back .brand-name { color: var(--ink); font-size: 40px; }
  .owner-names {
    top: 322px; font-family: "Poppins", sans-serif; font-weight: 700; color: var(--orange);
    font-size: 30px; line-height: 31px;
  }
  .owner-role { top: 390px; font-size: 20px; }
  .abn { top: 428px; font-size: 31px; }
  .abn strong { font-family: "Poppins", sans-serif; font-weight: 700; }
  .street-address { top: 484px; font-size: 18px; line-height: 19px; }

  .contact-rail { position: absolute; left: 613px; top: 275px; width: 2px; height: 218px; background: var(--ink); }
  .contact-list { list-style: none; }
  .contact-item { position: absolute; left: 0; width: 1000px; height: 0; }
  .contact-icon {
    position: absolute; left: 598px; top: -16px; width: 32px; height: 32px; border-radius: 50%;
    background: var(--ink); display: flex; align-items: center; justify-content: center;
  }
  .contact-icon.small { left: 604px; top: -10px; width: 20px; height: 20px; }
  .contact-icon svg { display: block; }
  .contact-text {
    position: absolute; left: 643px; top: -14px; color: var(--white); font-size: 22px; line-height: 22px; white-space: nowrap;
  }
  .contact-text.bold { font-family: "Poppins", sans-serif; font-weight: 700; font-size: 21px; top: -13px; }
  .contact-text.two-line { top: -22px; line-height: 21px; }
</style>
</head>
<body>

<section class="card card-front" aria-label="Business card front">
  <div class="brand-front">
    <span class="brand-dot"></span>
    <span class="brand-name">Gumtree Engine Works</span>
  </div>
  <div class="front-dots">•••</div>
  <div class="front-web">www.<strong>gewservice</strong>.com.au</div>
  <svg class="front-band" viewBox="0 0 1000 18" aria-hidden="true">
    <rect x="0" y="0" width="1000" height="18" fill="#9a9a9a"/>
    <polygon points="295,0 710,0 698,18 307,18" fill="#0a0a0a"/>
    <rect x="305" y="10" width="395" height="8" fill="#ec6e22"/>
  </svg>
</section>

<section class="card card-back" aria-label="Business card back">
  <div class="back-panel"></div>
  <svg class="panel-notch" viewBox="0 0 22 36" aria-hidden="true"><polygon points="0,0 22,18 0,36" fill="#f7f7f7"/></svg>

  <div class="brand-back">
    <span class="brand-dot"></span>
    <span class="brand-name">Gumtree Engine Works</span>
  </div>
  <div class="back-id owner-names">DOUG &amp;<br>MARISOL BRENT-COYLE</div>
  <div class="back-id owner-role">Owners/Directors</div>
  <div class="back-id abn">ABN: <strong>41 917 302 846</strong></div>
  <div class="back-id street-address">317 Wattlebrook Street CHARTERS TOWERS<br>QLD 4820 Postal</div>

  <div class="contact-rail"></div>
  <ul class="contact-list">
    <li class="contact-item" style="top:94px">
      <span class="contact-icon"><svg width="16" height="18" viewBox="0 0 16 18"><path d="M8 1a6 6 0 0 0-6 6c0 4.5 6 10 6 10s6-5.5 6-10a6 6 0 0 0-6-6z" fill="none" stroke="#ec6e22" stroke-width="2"/><circle cx="8" cy="7" r="2" fill="#ec6e22"/></svg></span>
      <span class="contact-text two-line">PO Box 5791 CHARTERS<br>TOWERS QLD 4820</span>
    </li>
    <li class="contact-item" style="top:145px">
      <span class="contact-icon"><svg width="16" height="16" viewBox="0 0 16 16"><path d="M3 1l3 3-2 2c1 2.5 3.5 5 6 6l2-2 3 3-2 2C7 15 1 9 1 3z" fill="#ec6e22"/></svg></span>
      <span class="contact-text bold">4712 9083</span>
    </li>
    <li class="contact-item" style="top:189px">
      <span class="contact-icon"><svg width="16" height="16" viewBox="0 0 16 16"><path d="M3 1l3 3-2 2c1 2.5 3.5 5 6 6l2-2 3 3-2 2C7 15 1 9 1 3z" fill="#ec6e22"/></svg></span>
      <span class="contact-text bold">0438 175 906</span>
    </li>
    <li class="contact-item" style="top:231px">
      <span class="contact-icon"><svg width="18" height="18" viewBox="0 0 18 18" fill="none" stroke="#ec6e22" stroke-width="1.6"><circle cx="9" cy="9" r="7.5"/><ellipse cx="9" cy="9" rx="3.2" ry="7.5"/><path d="M1.5 9h15M3 5h12M3 13h12"/></svg></span>
      <span class="contact-text">www.gewservice.com.au</span>
    </li>
    <li class="contact-item" style="top:275px">
      <span class="contact-icon"><svg width="16" height="12" viewBox="0 0 16 12"><rect x="0" y="0" width="16" height="12" rx="1.5" fill="#ec6e22"/><path d="M1 1l7 6 7-6" fill="none" stroke="#141414" stroke-width="1.6"/></svg></span>
      <span class="contact-text">sales@gewservice.com.au</span>
    </li>
    <li class="contact-item" style="top:317px">
      <span class="contact-icon small"><svg width="10" height="8" viewBox="0 0 16 12"><rect width="16" height="12" rx="1.5" fill="#ec6e22"/><path d="M1 1l7 6 7-6" fill="none" stroke="#141414" stroke-width="2"/></svg></span>
      <span class="contact-text">admin@gewservice.com.au</span>
    </li>
    <li class="contact-item" style="top:360px">
      <span class="contact-icon small"><svg width="10" height="8" viewBox="0 0 16 12"><rect width="16" height="12" rx="1.5" fill="#ec6e22"/><path d="M1 1l7 6 7-6" fill="none" stroke="#141414" stroke-width="2"/></svg></span>
      <span class="contact-text">accounts@gewservice.com.au</span>
    </li>
    <li class="contact-item" style="top:404px">
      <span class="contact-icon small"><svg width="10" height="8" viewBox="0 0 16 12"><rect width="16" height="12" rx="1.5" fill="#ec6e22"/><path d="M1 1l7 6 7-6" fill="none" stroke="#141414" stroke-width="2"/></svg></span>
      <span class="contact-text">parts@gewservice.com.au</span>
    </li>
    <li class="contact-item" style="top:449px">
      <span class="contact-icon small"><svg width="10" height="8" viewBox="0 0 16 12"><rect width="16" height="12" rx="1.5" fill="#ec6e22"/><path d="M1 1l7 6 7-6" fill="none" stroke="#141414" stroke-width="2"/></svg></span>
      <span class="contact-text">office@gewservice.com.au</span>
    </li>
    <li class="contact-item" style="top:493px">
      <span class="contact-icon"><svg width="16" height="12" viewBox="0 0 16 12"><rect width="16" height="12" rx="1.5" fill="#ec6e22"/><path d="M1 1l7 6 7-6" fill="none" stroke="#141414" stroke-width="1.6"/></svg></span>
      <span class="contact-text">reception@gewservice.com.au</span>
    </li>
  </ul>
</section>

</body>
</html>
```